Tervolan Pty Ltd professional business card

A professional business card template using the colours from the supplied logo.
Clean crisp lines while, Modern while not being over the top.

Target Market(s)

Construction, commerical and industrial

Industry/Entity Type

Communications

Contact Information for Business Card

For a Communications, IT, Optical fibre installation company

Colors
37b8a4

```html
<!DOCTYPE html>
<html lang="en">
<head>
<meta charset="utf-8">
<title>Tervolan Pty Ltd – Business Card</title>
<link href="https://fonts.googleapis.com/css2?family=Montserrat:wght@500;700&display=swap" rel="stylesheet">
<style>
  :root {
    --bg: #1f1f21;
    --teal: #1e93a0;
    --grey: #6b6e72;
    --brand-grey: #5e6166;
    --white: #ffffff;
  }
  * { margin: 0; padding: 0; box-sizing: border-box; }
  html, body { width: 1200px; height: 900px; overflow: hidden; }
  body {
    background: var(--bg);
    font-family: "Montserrat", Arial, sans-serif;
    position: relative;
  }
  .card {
    position: absolute;
    left: 280px;
    width: 640px;
    height: 366px;
    overflow: hidden;
    box-shadow: 0 10px 30px rgba(0,0,0,0.5);
  }
  .card-front { top: 64px; background: var(--teal); }
  .card-back { top: 470px; background: var(--white); }

  .brand-name {
    position: absolute;
    font-weight: 500;
    color: var(--brand-grey);
    letter-spacing: 2px;
    line-height: 1;
  }
  .card-front .brand-name { right: 52px; top: 160px; font-size: 46px; }
  .card-back .brand-name { left: 48px; top: 52px; font-size: 34px; }

  .accent-band {
    position: absolute;
    left: 0;
    right: 0;
    top: 150px;
    bottom: 0;
    background: linear-gradient(100deg, var(--teal) 0%, var(--teal) 30%, var(--grey) 55%, var(--grey) 100%);
  }

  .contact-block {
    position: absolute;
    right: 36px;
    top: 172px;
    text-align: right;
    color: var(--white);
  }
  .person-name { font-size: 15px; font-weight: 700; letter-spacing: 0.5px; }
  .person-title { font-size: 12.5px; font-weight: 500; margin-bottom: 14px; }
  .contact-list { list-style: none; }
  .contact-list li {
    font-size: 12.5px;
    font-weight: 500;
    height: 20px;
    display: flex;
    align-items: center;
    justify-content: flex-end;
    gap: 8px;
  }
  .contact-list li.gap-before { margin-top: 8px; }
  .icon { width: 14px; height: 14px; flex: none; }
  .icon-blank { width: 14px; flex: none; }
</style>
</head>
<body>

<section class="card card-front" aria-label="Business card front">
  <div class="brand-name">TERVOLAN</div>
</section>

<section class="card card-back" aria-label="Business card back">
  <div class="accent-band" role="img" aria-label="Teal and grey sweeping wave decoration"></div>

  <div class="brand-name">TERVOLAN</div>

  <div class="contact-block">
    <div class="person-name">DANIEL MARSH</div>
    <div class="person-title">Project Manager</div>
    <ul class="contact-list">
      <li>02 8145 3962
        <svg class="icon" viewBox="0 0 16 16" fill="none" stroke="currentColor" stroke-width="1.3"><circle cx="8" cy="8" r="6.5"/><path d="M5.5 4.5c-.6.6-.4 2 .9 3.6 1.4 1.6 2.9 2.3 3.6 1.7l.6-.7-1.4-1.2-.7.5c-.6-.2-1.5-1.1-1.8-1.8l.5-.7L6 4.4z"/></svg>
      </li>
      <li>daniel@tervolanptyltd.com
        <svg class="icon" viewBox="0 0 16 16" fill="none" stroke="currentColor" stroke-width="1.3"><rect x="1.5" y="3.5" width="13" height="9"/><path d="M1.5 3.5 8 9l6.5-5.5"/></svg>
      </li>
      <li>www.tervolanptyltd.com
        <svg class="icon" viewBox="0 0 16 16" fill="none" stroke="currentColor" stroke-width="1.3"><circle cx="8" cy="8" r="6.5"/><ellipse cx="8" cy="8" rx="2.8" ry="6.5"/><path d="M1.5 8h13M2.5 5h11M2.5 11h11"/></svg>
      </li>
      <li class="gap-before">PO Box 48215, Sydney. AU<span class="icon-blank"></span></li>
      <li>@tervolanfibre
        <svg class="icon" viewBox="0 0 16 16" fill="none" stroke="currentColor" stroke-width="1.3"><circle cx="8" cy="8" r="6"/></svg>
      </li>
    </ul>
  </div>
</section>

</body>
</html>
```